MBRCCUL re-branding website and logo

We are looking for a new webpage design and logo our current page address is www.mbrccul-example.org. We want to create a new design using MBRCCUL Mariners and Bakers Regional Co-operative Credit Union limited and another with the purposed new name MBFC Mariners and Bakers Financial Co-operative, the color scheme is purple and burnt orange. Our new logo and webpage should communicate change and growth purposed theme continuing our legacy here to server past, present and future generations. Our idea for the logo is a live shot of hands of different ages in a circle holding a tree

Target Market(s)

Everyone

Contact Information for Business Card

Company Name
Telephone number
Address
slot to enter employee info

Logo Text

(M & B) Mariners And Bakers Financial Co-operative

Coding

Coded - Design and coding required

Number of Pages Required

2 page

Colors
f37122
fbed22
6b449b

Requirements
Must have
• links for social media

```html
<!DOCTYPE html>
<html lang="en">
<head>
<meta charset="utf-8">
<title>MBFC Mariners and Bakers Financial Co-operative</title>
<link href="https://fonts.googleapis.com/css2?family=Roboto:wght@300;400;500;700&display=swap" rel="stylesheet">
<style>
:root{
  --orange:#f37122;
  --orange-deep:#ee5a1c;
  --yellow:#fbd922;
  --purple:#6b449b;
  --black:#000;
  --ink:#333;
  --muted:#888;
  --light:#f4f5f7;
  --white:#fff;
}
*{margin:0;padding:0;box-sizing:border-box}
html,body{width:725px;height:1200px;overflow:hidden}
body{font-family:"Roboto",Arial,sans-serif;background:var(--white);position:relative;color:var(--ink)}
.abs{position:absolute}

/* header */
.site-header{left:0;top:0;width:725px;height:70px;background:var(--black)}
.contact-tab{left:445px;top:0;width:280px;height:27px;background:var(--orange);clip-path:polygon(0 0,100% 0,100% 100%,22px 100%);color:var(--white);font-size:7.5px;font-weight:500;display:flex;align-items:center;gap:10px;padding-left:34px}
.contact-tab span{display:flex;align-items:center;gap:6px}
.contact-tab .sep{width:1px;height:10px;background:rgba(255,255,255,.7)}
.brand{left:52px;top:8px;display:flex;align-items:center;gap:4px}
.brand-dot{width:40px;height:40px;border-radius:50%;background:#7d8a58}
.brand-name{color:var(--white);font-weight:700;font-size:20px;line-height:1}
.brand-sub{left:92px;top:56px;color:#aaa;font-size:3.6px;letter-spacing:.6px;line-height:1.3;width:70px}
.main-nav{left:195px;top:45px;display:flex;gap:14px;color:var(--white);font-size:7px;font-weight:500}

/* hero */
.hero{left:0;top:70px;width:725px;height:296px;background:linear-gradient(120deg,#c9cbcf 0%,#9ea3ab 45%,#5f6673 75%,#2f3744 100%)}
.hero-title{left:0;top:172px;width:725px;text-align:center;color:var(--white);font-size:19px;line-height:1.45;text-shadow:0 1px 3px rgba(0,0,0,.25)}
.hero-title b{font-weight:500}
.hero-title span{font-weight:300}

/* feature cards */
.card{top:303px;width:202px;height:138px;color:var(--white);text-align:center;padding-top:12px;box-shadow:0 2px 4px rgba(0,0,0,.15)}
.card h3{font-size:11.5px;font-weight:500;margin:8px 0 7px}
.card p{font-size:7.2px;line-height:14.5px;padding:0 14px}
.card-loan{left:52px;background:linear-gradient(#f37122,#ee5a1c)}
.card-member{left:261px;background:linear-gradient(#fbe526,#f4c615)}
.card-calc{left:471px;background:linear-gradient(#7a50ad,#5c3889)}

/* welcome + rates */
.welcome{left:52px;top:465px;width:343px}
.welcome h2,.rates h2{font-size:13px;font-weight:400;color:#444}
.notice{color:var(--orange);font-size:10px;font-weight:300;margin-top:6px}
.expiry{color:var(--purple);font-size:7.2px;font-weight:500;margin-top:6px}
.body-text{color:var(--muted);font-size:7.2px;line-height:14.5px;margin-top:9px}
.rates{left:423px;top:465px;width:250px}
.rates .body-text{margin-top:7px}
.rate-table{width:100%;margin-top:10px;border-collapse:collapse;font-size:7.2px;color:#555}
.rate-table td{height:21px;border-bottom:1px solid #eee}
.rate-table .dash{text-align:center;width:40px;color:#999}
.rate-table .val{text-align:right;color:var(--orange);font-weight:700;font-size:9px}

/* news */
.news{left:0;top:650px;width:725px;height:323px;background:var(--light)}
.news-head{left:0;top:667px;width:725px;text-align:center}
.news-head h2{font-size:13px;font-weight:400;color:#444}
.news-head p{font-size:7px;color:var(--muted);margin-top:5px}
.post{top:712px;width:197px}
.post-photo{width:197px;height:124px}
.post h3{font-size:9px;font-weight:500;color:#333;margin-top:15px;padding-bottom:6px;border-bottom:1px solid #e2e2e2}
.post-meta{display:flex;justify-content:space-between;font-size:5.2px;color:#999;padding:6px 2px 0}
.post p{font-size:7.2px;line-height:15px;color:#666;margin-top:10px}

/* newsletter */
.newsletter{left:0;top:973px;width:725px;height:66px;background:var(--orange)}
.newsletter h2{left:93px;top:22px;color:var(--white);font-size:19px;font-weight:500}
.email-field{left:343px;top:21px;width:224px;height:24px;background:var(--white);border-radius:2px;font-size:7.2px;color:#999;padding:8px 11px}
.subscribe-btn{left:571px;top:21px;width:69px;height:24px;background:var(--black);color:var(--white);font-size:8px;font-weight:500;text-align:center;line-height:24px;border-radius:2px}

/* footer */
.site-footer{left:0;top:1039px;width:725px;height:161px;background:var(--black);color:var(--white)}
.foot-brand{left:52px;top:1055px;display:flex;align-items:center;gap:2px}
.foot-brand .brand-dot{width:53px;height:53px}
.foot-brand .brand-name{font-size:24px}
.foot-sub{left:101px;top:1127px;color:#aaa;font-size:4px;letter-spacing:.7px;line-height:1.3;width:90px}
.foot-col{top:1061px;font-size:7.2px;line-height:14px}
.foot-col h4{font-size:8.5px;font-weight:500;margin-bottom:9px}
.foot-col p{margin-bottom:4px}
.social{display:flex;gap:4px;margin-top:9px}
.social i{width:18px;height:18px;border:1px solid var(--white);border-radius:50%}
.foot-rule{left:52px;top:1162px;width:621px;height:1px;background:#333}
.copyright{left:0;top:1175px;width:725px;text-align:center;color:var(--white);font-size:7.2px}
</style>
</head>
<body>

<header class="abs site-header"></header>
<div class="abs contact-tab">
  <span><svg width="9" height="9" viewBox="0 0 24 24"><path fill="#fff" d="M6.6 10.8a15 15 0 0 0 6.6 6.6l2.2-2.2c.3-.3.7-.4 1-.2 1.1.4 2.3.6 3.6.6.6 0 1 .4 1 1V20c0 .6-.4 1-1 1A17 17 0 0 1 3 4c0-.6.4-1 1-1h3.5c.6 0 1 .4 1 1 0 1.3.2 2.5.6 3.6.1.3 0 .7-.2 1z"/></svg>PHONE: (242) 555-0140</span>
  <i class="sep"></i>
  <span><svg width="9" height="9" viewBox="0 0 24 24"><rect x="3" y="8" width="18" height="12" rx="1" fill="#fff"/><rect x="7" y="3" width="10" height="6" fill="#fff"/><rect x="6" y="12" width="3" height="2" fill="#f37122"/></svg>FAX: (242) 555-0141</span>
</div>
<div class="abs brand"><div class="brand-dot" role="img" aria-label="Brand emblem area"></div><div class="brand-name">M &amp; B</div></div>
<div class="abs brand-sub">MARINERS &amp; BAKERS<br>FINANCIAL CO-OPERATIVE</div>
<nav class="abs main-nav">
  <span>HOME</span><span>MY CREDIT UNION ▾</span><span>PRODUCTS &amp; SERVICES ▾</span><span>TOOL &amp; BENEFITS ▾</span><span>APPLY FOR A LOAN</span><span>BECOME A MEMBER</span><span>LOCATIONS</span>
</nav>

<section class="abs hero" role="img" aria-label="Photo of hands working on a laptop with financial charts overlay"></section>
<h1 class="abs hero-title"><b>MBFC MARINERS</b><br><span>AND BAKERS FINANCIAL CO-OPERATIVE</span></h1>

<div class="abs card card-loan">
  <svg width="42" height="38" viewBox="0 0 42 38"><rect x="6" y="4" width="24" height="30" rx="2" fill="none" stroke="#fff" stroke-width="2.5"/><path d="M11 12h14M11 18h10M11 24h7" stroke="#fff" stroke-width="2.5"/><path d="M22 30l14-16 4 3-14 16-5 1z" fill="#fff"/></svg>
  <h3>APPLY FOR A LOAN</h3>
  <p>We are an Open Bond Credit Union. Anyone can join who is earning a salary or source supporting evidence/documentation.</p>
</div>
<div class="abs card card-member">
  <svg width="48" height="38" viewBox="0 0 48 38"><circle cx="24" cy="11" r="8" fill="#fff"/><circle cx="12" cy="14" r="6" fill="#fff"/><circle cx="36" cy="14" r="6" fill="#fff"/><path d="M10 36c0-9 6-15 14-15s14 6 14 15z" fill="#fff"/><path d="M1 34c0-7 5-11 11-11 2 0 3 0 4 1-3 3-5 6-5 10zM47 34c0-7-5-11-11-11-2 0-3 0-4 1 3 3 5 6 5 10z" fill="#fff"/></svg>
  <h3>BECAME A MEMBER</h3>
  <p>We are an Open Bond Credit Union. Anyone can join who is earning a salary or source supporting evidence/documentation.</p>
</div>
<div class="abs card card-calc">
  <svg width="44" height="40" viewBox="0 0 44 40"><text x="2" y="20" fill="#fff" font-size="22" font-weight="700" font-family="Roboto,sans-serif">$</text><rect x="16" y="10" width="22" height="30" rx="2" fill="#fff"/><rect x="19" y="13" width="16" height="6" fill="#6b449b"/><g fill="#6b449b"><rect x="19" y="22" width="4" height="4"/><rect x="25" y="22" width="4" height="4"/><rect x="31" y="22" width="4" height="4"/><rect x="19" y="28" width="4" height="4"/><rect x="25" y="28" width="4" height="4"/><rect x="31" y="28" width="4" height="4"/><rect x="19" y="34" width="4" height="3"/><rect x="25" y="34" width="4" height="3"/><rect x="31" y="34" width="4" height="3"/></g></svg>
  <h3>FINANCIAL CALCULATORS</h3>
  <p>We are an Open Bond Credit Union. Anyone can join who is earning a salary or source supporting evidence/documentation.</p>
</div>

<section class="abs welcome">
  <h2>Welcome to ATM Cards Renewal Notice</h2>
  <p class="notice">PLEASE BE ADVISED THAT ALL ATM CARDS ISSUED FEBRUARY 2014</p>
  <p class="expiry">EXPIRES EFFECTIVE FEBRUARY 28,2017</p>
  <p class="body-text">All applicants for Mortgages must be able to demonstrate that the loan can be repaid on a monthly basis from a salary assignment.&nbsp; Over the counter payments will no lon ger be accepted either as the full source of repayment or to augment partial salary deductions on Mortgage</p>
  <p class="body-text">The principle upon which the credit union was built revolutionized Banking in The Bahamas. For the first time, a credit union would become a financial partner to the working Bahamian. Members could and receive high interest and It is a place where Bahamians are financially dividends.</p>
</section>

<section class="abs rates">
  <h2>Featured Rates</h2>
  <p class="body-text">All applicants for Mortgages must be able to demonstrate that the loan can be repaid on a monthly basis from a salary assignment.&nbsp; Over the counter payments will no lon ger be accepted either...</p>
  <table class="rate-table">
    <tr><td>Consumer Loans as low as</td><td class="dash">-</td><td class="val">9.00% APR*</td></tr>
    <tr><td>New Auto/Motorcycle as low as</td><td class="dash">-</td><td class="val">7.00% APR*</td></tr>
    <tr><td>Used Auto/Motorcycle</td><td class="dash">-</td><td class="val">11.75% APR*</td></tr>
    <tr><td>Mortgages as low as</td><td class="dash">-</td><td class="val">8.25% APR*</td></tr>
  </table>
</section>

<section class="abs news"></section>
<div class="abs news-head">
  <h2>News &amp; Events</h2>
  <p>All applicants for Mortgages must be able to demonstrate that the loan can be repaid on a monthly</p>
</div>

<article class="abs post" style="left:52px">
  <div class="post-photo" role="img" aria-label="Photo of a laptop and financial papers on a desk" style="background:linear-gradient(135deg,#6b5a4a,#c9b8a2 55%,#e8e4df)"></div>
  <h3>MUST BE A MEMBER OF THE CREDIT UNION</h3>
  <div class="post-meta"><span>◷ 27 MARCH 2017</span><span>◌ 120</span><span>♡ LIKE</span><span>⇱ SHARE</span></div>
  <p>The principle upon which the credit union was built revo lutionized Banking in The Bahamas. For the first time, a credit union would become a financial....</p>
</article>
<article class="abs post" style="left:264px">
  <div class="post-photo" role="img" aria-label="Illustration of rising bar charts and financial graphs" style="background:linear-gradient(135deg,#2f7f8f,#8fcbd8 55%,#e6f3f6)"></div>
  <h3>MUST BE A MEMBER OF THE CREDIT UNION</h3>
  <div class="post-meta"><span>◷ 27 MARCH 2017</span><span>◌ 120</span><span>♡ LIKE</span><span>⇱ SHARE</span></div>
  <p>The principle upon which the credit union was built revo lutionized Banking in The Bahamas. For the first time, a credit union would become a financial....</p>
</article>
<article class="abs post" style="left:476px">
  <div class="post-photo" role="img" aria-label="Photo of printed charts with a pen and notebook" style="background:linear-gradient(135deg,#8a929c,#cdd5df 55%,#eef1f5)"></div>
  <h3>MUST BE A MEMBER OF THE CREDIT UNION</h3>
  <div class="post-meta"><span>◷ 27 MARCH 2017</span><span>◌ 120</span><span>♡ LIKE</span><span>⇱ SHARE</span></div>
  <p>The principle upon which the credit union was built revo lutionized Banking in The Bahamas. For the first time, a credit union would become a financial....</p>
</article>

<section class="abs newsletter">
  <h2 class="abs">NEWSLETTER SUBSCRIBE :</h2>
  <div class="abs email-field">Enter Your Email Id :</div>
  <div class="abs subscribe-btn">SUBSCRIBE</div>
</section>

<footer class="abs site-footer"></footer>
<div class="abs foot-brand"><div class="brand-dot" role="img" aria-label="Brand emblem area"></div><div class="brand-name">M &amp; B</div></div>
<div class="abs foot-sub">MARINERS &amp; BAKERS<br>FINANCIAL CO-OPERATIVE</div>
<div class="abs foot-col" style="left:207px;width:90px;color:#fff">
  <h4>NASSAU</h4>
  <p>Location: Harbour Lane &amp; Mill Road</p><p>Phone: (242) 555-0140</p><p>Fax: (242) 555-0141</p>
</div>
<div class="abs foot-col" style="left:315px;width:130px;color:#fff">
  <h4>FREEPORT, GRAND BAHAMA</h4>
  <p>Location: #8 Quayside Dr.</p><p>Phone: (242) 555-0152</p><p>Fax: (242) 555-0153</p>
</div>
<div class="abs foot-col" style="left:464px;width:90px;color:#fff">
  <h4>ABACO</h4>
  <p>Location: Cedar Point Shopping Centre</p><p>Phone: (242) 555-0164</p><p>Fax: (242) 555-0165</p>
</div>
<div class="abs foot-col" style="left:568px;width:110px;color:#fff">
  <h4>FOLLOW US</h4>
  <p>The principle upon which the credit union was built revo lutionized Banking</p>
  <div class="social"><i></i><i></i><i></i><i></i><i></i></div>
</div>
<div class="abs foot-rule"></div>
<div class="abs copyright">Copyright © 2017 Mariners &amp; Bakers Regional Co-operative Credit Union Ltd. All Rights Reserved.</div>

</body>
</html>
```